Non Profit Company Looking For New Website

The website for Corvelle Brightwater Renewal Society should offer the viewer beautiful photos that inspire condifence and joy and tap into our love of horses.

We would like to see a website that displays trust, quality and confidence. Needs to be responsive and mobile friendly for all browsers and coded for both Android & IOS.

READ ATTACHED WEBSITE TEMPLATE FOR COMPLETE DETAILS ON WHAT WE ARE LOOKING FOR.

Looking for recommmendations if we should use WordPress/WooCommerce for site or Wordpress with Shopify Plug in or just Shopify.

Must be both desktop and mobile friendly with fast page load speed. Need the ability to edit ourselves.

Industry/Entity Type

Non Profit

Coding

Coded - Design and coding required

Number of Pages Required

5+ page

Requirements
Must have
• We would like to see a website that displays trust, quality and confidence. Needs to be responsive and mobile friendly for all browsers and coded for both Android & IOS.

Looking for recommendations if we should use WordPress/WooCommerce for site or Wordpress with Shopify Plug in or just Shopify.

Logo Colour:
Pantone 7621 C

READ TEMPLATE THAT IS ATTACHED
Nice to have
• Like look of this website as a sample:
https://www.velmontquarry.com/

Another similar non profit organization
https://tamberlockfields.com/

```html
<!DOCTYPE html>
<html lang="en">
<head>
<meta charset="utf-8">
<title>Corvelle Brightwater Renewal Society — Website</title>
<link rel="stylesheet" href="https://fonts.googleapis.com/css2?family=Playfair+Display:wght@700&family=Merriweather:wght@400;700&display=swap">
<style>
  :root{
    --stage:#a9222a;
    --brand:#b31d2a;
    --white:#ffffff;
    --ink:#222222;
    --nav:#4a4a4a;
    --green:#1cbc4c;
    --pasture-dark:#26391a;
    --pasture-mid:#34501f;
    --pasture-light:#3e5d25;
    --section-grey:#f3f3f3;
  }
  *{box-sizing:border-box;margin:0;padding:0}
  html,body{width:1200px;height:517px;overflow:hidden}
  body{background:var(--stage);position:relative;font-family:"Merriweather",Georgia,serif}

  .screen{position:absolute;background:var(--white);overflow:hidden}
  .screen--desktop{left:106px;top:28px;width:820px;height:442px}
  .screen--mobile{left:951px;top:140px;width:161px;height:330px}

  .site-header{position:relative;display:flex;align-items:center;background:var(--white)}
  .screen--desktop .site-header{height:56px;padding:0 32px 0 27px;justify-content:space-between}
  .screen--mobile .site-header{height:59px;padding:0 8px 0 8px;justify-content:space-between}

  .brand-name{color:var(--brand);font-weight:400;text-align:center;text-transform:uppercase;letter-spacing:.3px}
  .screen--desktop .brand-name{font-size:5.6px;line-height:7.5px;width:52px}
  .screen--mobile .brand-name{font-size:5px;line-height:6.8px;width:46px}

  .main-nav{display:flex;gap:17px}
  .main-nav a{font-size:6px;letter-spacing:.3px;color:var(--nav);text-decoration:none;text-transform:uppercase}
  .main-nav a.is-active{color:var(--brand);font-weight:700}

  .menu-toggle{display:flex;align-items:center;gap:3px;font-size:6px;color:var(--nav);text-transform:uppercase}

  .hero{position:relative;text-align:center;color:var(--white)}
  .screen--desktop .hero{height:318px}
  .screen--mobile .hero{height:271px}
  .hero-photo{position:absolute;inset:0;background:
      radial-gradient(ellipse at 62% 55%, rgba(90,55,25,.35), transparent 45%),
      linear-gradient(180deg,var(--pasture-dark) 0%,var(--pasture-mid) 45%,var(--pasture-light) 100%)}
  .hero-content{position:relative;display:flex;flex-direction:column;align-items:center}
  .hero-title{font-family:"Playfair Display",Georgia,serif;font-weight:700}
  .screen--desktop .hero-content{padding-top:80px}
  .screen--desktop .hero-title{font-size:31px;line-height:30.5px;width:520px}
  .screen--mobile .hero-content{padding-top:37px}
  .screen--mobile .hero-title{font-size:18.5px;line-height:19px;width:150px}

  .hero-actions{display:flex;gap:4px;align-items:center}
  .screen--desktop .hero-actions{margin-top:40px}
  .screen--mobile .hero-actions{flex-direction:column;gap:5px;margin-top:28px}
  .btn{display:inline-flex;align-items:center;justify-content:center;height:25px;border-radius:13px;font-size:8px;font-weight:700;text-decoration:none}
  .btn--outline{width:108px;border:1px solid var(--green);color:var(--green);background:transparent}
  .btn--solid{width:53px;background:var(--green);color:var(--white)}

  .intro{background:var(--section-grey);height:68px;text-align:center}
  .intro-title{font-family:"Playfair Display",Georgia,serif;font-weight:700;font-size:29px;color:var(--ink);padding-top:40px;line-height:30px}
</style>
</head>
<body>

  <section class="screen screen--desktop" aria-label="Desktop home page">
    <header class="site-header">
      <div class="brand-name">Corvelle Brightwater Renewal Society</div>
      <nav class="main-nav">
        <a class="is-active" href="#">Home</a>
        <a href="#">About</a>
        <a href="#">Adopt</a>
        <a href="#">Horses</a>
        <a href="#">Donate &amp; Shop</a>
        <a href="#">Contact</a>
      </nav>
    </header>
    <div class="hero">
      <div class="hero-photo" role="img" aria-label="Photo of thoroughbred horses walking through a green pasture"></div>
      <div class="hero-content">
        <h1 class="hero-title">We support and develop retired thoroughbred racehorses for their next chapter in life</h1>
        <div class="hero-actions">
          <a class="btn btn--outline" href="#">Adopt a thoroughbred</a>
          <a class="btn btn--solid" href="#">Donate</a>
        </div>
      </div>
    </div>
    <section class="intro">
      <h2 class="intro-title">Retire. Retrain.</h2>
    </section>
  </section>

  <section class="screen screen--mobile" aria-label="Mobile home page">
    <header class="site-header">
      <div class="brand-name">Corvelle Brightwater Renewal Society</div>
      <div class="menu-toggle">Menu
        <svg width="7" height="6" viewBox="0 0 7 6" aria-hidden="true"><path d="M0 .5h7M0 3h7M0 5.5h7" stroke="#4a4a4a" stroke-width=".8"/></svg>
      </div>
    </header>
    <div class="hero">
      <div class="hero-photo" role="img" aria-label="Photo of thoroughbred horses grazing in a green pasture"></div>
      <div class="hero-content">
        <h1 class="hero-title">We support and develop retired thoroughbred racehorses for their next chapter in life</h1>
        <div class="hero-actions">
          <a class="btn btn--outline" href="#">Adopt a thoroughbred</a>
          <a class="btn btn--solid" href="#">Donate</a>
        </div>
      </div>
    </div>
  </section>

</body>
</html>
```